Window Tinting Website Design

We are working with a Window Tinting company in California. They do commercial, residential, and automotive tint.

Some websites for inspiration:
https://www.velmoshadez.com/
https://www.qpridegleam.com/
https://drobfinishx.com/

Thank you for taking the time to consider designing a website for us. We are web developers based in Stockton, CA, USA. Most of our projects go through the same process. Understanding this process may help you win a project with us. We custom-code all of our websites in-house. We don’t have any requirements as to what tools you use for your design, but we ask that you follow these guidelines.

IMAGES:
If you use any images or icons in the design, we ask that you have a link to the asset so we can purchase the image/icon. Most of the designs we submit do not have the customer’s images on them unless they have some great images. Be creative; show us the feeling you are trying to portray with your image choices. Use any royalty-free site you choose. We subscribe to Brenlo and mainly use their images, but we can purchase images outside of Brenlo. PLEASE NOTE: we will not submit designs to clients with watermarks on the images.

FONTS:
We ask that you identify the fonts you’re using in the design. This can be done in a message if you want. We typically use plain circle badge Fonts and Brenlo Fonts.

CONTENT:
We're always open to different content and ideas. We often submit designs with stock images so the client can see our vision. We typically take pictures after the website launch to use their images with our vision. Lorem Ipsum is fine for paragraphs, but we ask that you make the Headers with correct English. We want to be able to show the vision and identify the sections of the website.

INSPIRATION:
We typically add a couple of links in the brief of websites we like to help you get started in your design.

REVISIONS:
We do not often ask for revisions of the designs unless we see something in the design that may not appeal to the client. If there are slight changes that we want to make, we do that in the development process.

FEEDBACK:
We rarely give feedback on designs during the design process. We are working on many website projects and do not have the time to provide feedback. We usually respond if your request is well thought out and asks specific questions, but a note asking “feedback, please” usually goes unanswered.

```html
<!DOCTYPE html>
<html lang="en">
<head>
<meta charset="utf-8">
<title>Halcyon Window Tinting</title>
<link href="https://fonts.googleapis.com/css2?family=Roboto:wght@400;500;700;900&display=swap" rel="stylesheet">
<style>
:root{
  --red:#c8001f;
  --red-dark:#a3001a;
  --slate:#46698c;
  --slate-text:#3d6489;
  --ink:#111;
  --body:#3b3b3b;
  --mist:#eef0f4;
  --white:#fff;
  --star:#f29a12;
}
*{box-sizing:border-box;margin:0;padding:0}
html,body{width:1200px;height:3916px;overflow:hidden}
body{font-family:'Roboto',sans-serif;color:var(--body);background:var(--white);position:relative}
.abs{position:absolute}
a{color:inherit;text-decoration:none}

/* header */
.site-header{position:absolute;top:0;left:0;width:1200px;height:100px;background:var(--white)}
.brand{position:absolute;left:98px;top:28px;font-weight:900;font-size:24px;color:var(--red);display:flex;align-items:center;gap:10px;line-height:1}
.brand .dot{width:26px;height:26px;border-radius:50%;background:var(--red)}
.topbar{position:absolute;top:8px;left:406px;display:flex;align-items:center;font-size:15px;color:#222}
.topbar .item{display:flex;align-items:center;gap:10px;margin-right:42px}
.topbar .ico{width:36px;height:36px;border-radius:50%;background:var(--slate);display:flex;align-items:center;justify-content:center}
.estimate{position:absolute;left:946px;top:8px;width:154px;height:34px;background:var(--slate);color:var(--white);font-size:16px;font-weight:500;display:flex;align-items:center;justify-content:center}
.navband{position:absolute;top:50px;left:322px;width:878px;height:50px}
.nav{position:absolute;top:50px;left:396px;height:50px;display:flex;align-items:center;gap:34px;color:var(--white);font-size:16px}

/* hero */
.hero{position:absolute;top:100px;left:0;width:1200px;height:620px}
.hero-copy{position:absolute;left:592px;top:135px;color:var(--white);width:500px}
.hero-copy h1{font-weight:700;font-size:52px;line-height:61px}
.hero-copy p{font-size:15px;line-height:31px;margin-top:6px;width:445px}
.btn-light{display:inline-flex;align-items:center;justify-content:center;width:137px;height:51px;background:var(--white);color:var(--ink);font-weight:700;font-size:17px;margin-top:16px}
.dots{position:absolute;left:1126px;top:236px;display:flex;flex-direction:column;gap:11px}
.dots span{width:11px;height:11px;border-radius:50%;background:var(--white)}
.dots span:first-child{background:var(--red)}

/* about */
.about h2{position:absolute;left:99px;top:772px;font-size:32px;font-weight:700;color:var(--ink)}
.accent{color:var(--red)}
.about p{position:absolute;left:99px;top:815px;width:492px;font-size:15.5px;line-height:31px}
.btn-slate{position:absolute;left:99px;top:1143px;width:137px;height:51px;background:var(--slate);color:var(--white);font-weight:700;font-size:17px;display:flex;align-items:center;justify-content:center;box-shadow:0 3px 6px rgba(0,0,0,.25)}
.about-mark{position:absolute;left:650px;top:850px;width:445px;height:265px;display:flex;align-items:center;justify-content:center;gap:16px;font-weight:900;font-size:46px;color:var(--red)}
.about-mark .dot{width:44px;height:44px;border-radius:50%;background:var(--red)}

/* financing */
.finance{position:absolute;top:1272px;left:0;width:1200px;height:486px;background:var(--red)}
.finance h2{position:absolute;left:656px;top:90px;font-size:32px;line-height:40px;font-weight:700;color:var(--white)}
.checks{position:absolute;left:656px;top:180px;list-style:none;color:var(--white);font-size:15.5px}
.checks li{display:flex;align-items:center;gap:24px;height:40.3px}

/* services */
.section-title{position:absolute;left:0;width:1200px;text-align:center;font-size:32px;font-weight:700;color:var(--ink)}
.card{position:absolute;top:1880px;width:318px;height:465px;background:var(--white);box-shadow:0 1px 5px rgba(0,0,0,.18)}
.card .photo{width:318px;height:245px}
.card .badge{position:absolute;left:14px;top:200px;width:80px;height:68px;background:var(--red);display:flex;align-items:center;justify-content:center}
.card h3{position:absolute;left:13px;top:289px;font-size:17px;font-weight:700;color:var(--slate-text);letter-spacing:.2px}
.card p{position:absolute;left:13px;top:317px;width:295px;font-size:15.5px;line-height:31px;color:#333}
.card .more{position:absolute;left:13px;top:417px;font-size:17px;font-weight:700;color:var(--slate-text);text-decoration:underline}

/* testimonials */
.testimonials{position:absolute;top:2430px;left:0;width:1200px;height:475px;background:var(--mist)}
.quote{position:absolute;top:170px;width:310px;height:190px;background:var(--white);border-radius:14px;border-top:3px solid var(--slate);box-shadow:0 3px 8px rgba(0,0,0,.12);text-align:center;font-size:15px;line-height:26px;color:#444;padding:64px 26px 0}
.avatar{position:absolute;top:125px;width:95px;height:95px;border-radius:50%;border:3px solid var(--white);background:radial-gradient(circle at 50% 40%,#d9c3b0,#8a8f99)}
.avatar .seal{position:absolute;right:-2px;bottom:0;width:28px;height:28px;border-radius:50%;background:var(--white);border:4px solid #4a86e8}
.reviewer{position:absolute;top:386px;font-size:16px;color:#222;display:flex;gap:22px;align-items:center}
.stars{color:var(--star);font-size:14px;letter-spacing:1px}
.arrow{position:absolute;top:2652px;width:28px;height:28px;border-radius:50%;background:#dde0e6;display:flex;align-items:center;justify-content:center}

/* contact */
.contact{position:absolute;top:2920px;left:0;width:1200px;height:617px;background:linear-gradient(180deg,#ececee 0%,#f4f4f5 45%,#e6e6e8 100%)}
.form-card{position:absolute;left:264px;top:127px;width:672px;height:430px;background:var(--white);border-radius:12px;box-shadow:0 2px 10px rgba(0,0,0,.08)}
.field{position:absolute;height:52px;border:1px solid #333;border-radius:6px;font-size:13px;color:#333;padding:18px 18px 0}
.field sup{color:var(--red);font-size:13px;vertical-align:top}
.submit{position:absolute;left:271px;top:307px;width:129px;height:50px;background:var(--red);color:var(--white);font-weight:700;font-size:16px;display:flex;align-items:center;justify-content:center}

/* footer */
.site-footer{position:absolute;top:3537px;left:0;width:1200px;height:379px;background:#000;color:var(--white)}
.footer-brand{position:absolute;left:0;width:1200px;top:120px;display:flex;justify-content:center;align-items:center;gap:12px;font-weight:900;font-size:34px;color:var(--red)}
.footer-brand .dot{width:32px;height:32px;border-radius:50%;background:var(--red)}
.footer-nav{position:absolute;left:0;width:1200px;top:240px;display:flex;justify-content:center;gap:34px;font-size:16px}
.copyright{position:absolute;left:0;width:1200px;top:296px;text-align:center;font-size:15px}
</style>
</head>
<body>

<header class="site-header">
  <div class="brand"><span class="dot"></span>Halcyon Tint</div>
  <div class="topbar">
    <div class="item"><span class="ico"><svg width="16" height="16" viewBox="0 0 24 24"><path fill="#fff" d="M6.6 10.8a15 15 0 0 0 6.6 6.6l2.2-2.2a1 1 0 0 1 1-.25 11.4 11.4 0 0 0 3.6.57 1 1 0 0 1 1 1V20a1 1 0 0 1-1 1A17 17 0 0 1 3 4a1 1 0 0 1 1-1h3.5a1 1 0 0 1 1 1c0 1.250.2 2.450.57 3.6a1 1 0 0 1-.25 1z"/></svg></span>Call Us:+1 555 0142 7788</div>
    <div class="item"><span class="ico"><svg width="16" height="14" viewBox="0 0 24 20"><path fill="#fff" d="M2 2h20a2 2 0 0 1 2 2v1l-12 7L0 5V4a2 2 0 0 1 2-2zm-2 6 12 7 12-7v10a2 2 0 0 1-2 2H2a2 2 0 0 1-2-2z"/></svg></span>Mail:info@halcyontint.com</div>
  </div>
  <a class="estimate">Get Free Estimate</a>
  <svg class="navband" viewBox="0 0 878 50"><polygon points="28,0 878,0 878,50 0,50" fill="#c8001f"/></svg>
  <nav class="nav"><a>Auto Tinting</a><a>Commercial Tinting</a><a>Home Tinting</a><a>Paint Protection</a><a>Detailing</a><a>Contact Us</a></nav>
</header>

<section class="hero">
  <svg width="1200" height="620" class="abs" style="left:0;top:0">
    <defs><linearGradient id="heroShade" x1="0" y1="0" x2="1" y2="0"><stop offset="0" stop-color="#3a4048"/><stop offset=".35" stop-color="#1e2226"/><stop offset="1" stop-color="#0e1012"/></linearGradient></defs>
    <polygon points="0,500 1200,500 1200,505 600,620 0,512" fill="#c8001f"/>
    <polygon points="0,0 1200,0 1200,502 600,590 0,505" fill="url(#heroShade)" role="img" aria-label="Technician applying tint film to a dark car window"/>
  </svg>
  <div class="hero-copy">
    <h1>Welcome To Window Tinting</h1>
    <p>Lorem ipsum dolor sit amet, consectetur adipiscing elit, sed do eiusmod tempor incididunt ut labore et dolore magna aliqua.</p>
    <a class="btn-light">Get Started</a>
  </div>
  <div class="dots"><span></span><span></span><span></span></div>
</section>

<section class="about">
  <h2>ABOUT <span class="accent">US</span></h2>
  <p>Sed ut perspiciatis unde omnis iste natus error sit voluptatem accusantium doloremque laudantium, totam rem aperiam, eaque ipsa quae ab illo inventore veritatis et quasi architecto beatae vitae dicta sunt explicabo. Nemo enim ipsam voluptatem quia voluptas sit aspernatur aut odit aut fugit, sed quia consequuntur magni dolores eos qui ratione voluptatem sequi nesciunt. Neque porro quisquam est, qui dolorem ipsum quia dolor sit amet, consectetur, adipisci velit, sed quia non numquam eius modi tempora incidunt ut labore et dolore magnam aliquam quaerat voluptatem. Ut enim ad minima veniam, quis nostrum laboriosam, nisi ut aliquid ex consequatur?</p>
  <a class="btn-slate">Read More</a>
  <div class="about-mark"><span class="dot"></span>Halcyon Tint</div>
</section>

<section class="finance">
  <svg width="627" height="486" class="abs" style="left:0;top:0">
    <defs><linearGradient id="finShade" x1="0" y1="0" x2="1" y2="1"><stop offset="0" stop-color="#4a4f57"/><stop offset=".6" stop-color="#2a2d33"/><stop offset="1" stop-color="#b0281f"/></linearGradient></defs>
    <polygon points="0,0 627,0 532,486 0,486" fill="url(#finShade)" role="img" aria-label="Installer fitting tint film on a red car in a lit workshop"/>
  </svg>
  <h2>WE NOW OFFER FINANCING<br>THROUGH PIVORA!</h2>
  <ul class="checks">
    <li><svg width="14" height="12" viewBox="0 0 14 12"><path d="M1 6.5 5 10 13 1.5" stroke="#fff" stroke-width="3" fill="none"/></svg>Lorem ipsum dolor sit amet, consectetur adipiscing elit</li>
    <li><svg width="14" height="12" viewBox="0 0 14 12"><path d="M1 6.5 5 10 13 1.5" stroke="#fff" stroke-width="3" fill="none"/></svg>Sed do eiusmod tempor incididunt ut labore et</li>
    <li><svg width="14" height="12" viewBox="0 0 14 12"><path d="M1 6.5 5 10 13 1.5" stroke="#fff" stroke-width="3" fill="none"/></svg>Ut enim ad minim veniam</li>
    <li><svg width="14" height="12" viewBox="0 0 14 12"><path d="M1 6.5 5 10 13 1.5" stroke="#fff" stroke-width="3" fill="none"/></svg>Excepteur sint occaecat cupidatat non proident</li>
    <li><svg width="14" height="12" viewBox="0 0 14 12"><path d="M1 6.5 5 10 13 1.5" stroke="#fff" stroke-width="3" fill="none"/></svg>Sed ut perspiciatis unde omnis iste</li>
    <li><svg width="14" height="12" viewBox="0 0 14 12"><path d="M1 6.5 5 10 13 1.5" stroke="#fff" stroke-width="3" fill="none"/></svg>Ut enim ad minima veniam, quis nostrum exercitationem</li>
  </ul>
</section>

<h2 class="section-title" style="top:1818px">OUR <span class="accent">SERVICES</span></h2>

<article class="card" style="left:98px">
  <div class="photo" role="img" aria-label="Tint film being applied to an office window overlooking city towers" style="background:linear-gradient(160deg,#9fc3e6,#c9d6df 55%,#8a6a55)"></div>
  <div class="badge"><svg width="40" height="40" viewBox="0 0 40 40" fill="none" stroke="#fff" stroke-width="2"><rect x="8" y="6" width="24" height="28"/><path d="M8 16h24M20 6v10M12 24h16M12 29h10"/></svg></div>
  <h3>COMMERCIAL TINTING</h3>
  <p>Ut enim ad minim veniam, quis nostrud exercitation ullamco laboris nisi ut aliquip ex ea commodo consequat.</p>
  <a class="more">Read More</a>
</article>
<article class="card" style="left:441px">
  <div class="photo" role="img" aria-label="Installer tinting a home window" style="background:linear-gradient(150deg,#e2dccf,#c7b89c 55%,#4f7bb0)"></div>
  <div class="badge"><svg width="40" height="40" viewBox="0 0 40 40" fill="none" stroke="#fff" stroke-width="2"><path d="M6 34 12 18h24l-6 16z"/><circle cx="27" cy="9" r="3"/><path d="M27 2v3M27 13v3M20 9h3M31 9h3M14 30l4-8"/></svg></div>
  <h3>RESIDENTIAL TINTING</h3>
  <p>Ut enim ad minim veniam, quis nostrud exercitation ullamco laboris nisi ut aliquip ex ea commodo consequat.</p>
  <a class="more">Read More</a>
</article>
<article class="card" style="left:784px">
  <div class="photo" role="img" aria-label="Hands stretching tint film over a car window" style="background:linear-gradient(160deg,#c9ccd0,#6d737a 55%,#3e444b)"></div>
  <div class="badge"><svg width="40" height="40" viewBox="0 0 40 40" fill="none" stroke="#fff" stroke-width="2"><path d="M8 26l3-8h18l3 8v7H8z"/><circle cx="13" cy="29" r="2"/><circle cx="27" cy="29" r="2"/><rect x="10" y="5" width="10" height="9"/></svg></div>
  <h3>AUTOMOTIVE TINT</h3>
  <p>Ut enim ad minim veniam, quis nostrud exercitation ullamco laboris nisi ut aliquip ex ea commodo consequat.</p>
  <a class="more">Read More</a>
</article>

<section class="testimonials">
  <h2 class="section-title" style="top:68px">TESTIMONIALS</h2>
  <div class="quote" style="left:112px">Sed ut perspiciatis unde omnis iste natus error sit voluptatem accusantium doloremque laudantium, totam rem aperiam, eaque ipsa</div>
  <div class="quote" style="left:445px">Sed ut perspiciatis unde omnis iste natus error sit voluptatem accusantium doloremque laudantium, totam rem aperiam, eaque ipsa</div>
  <div class="quote" style="left:778px">Sed ut perspiciatis unde omnis iste natus error sit voluptatem accusantium doloremque laudantium, totam rem aperiam, eaque ipsa</div>
  <div class="avatar" role="img" aria-label="Customer portrait" style="left:219px"><span class="seal"></span></div>
  <div class="avatar" role="img" aria-label="Customer portrait" style="left:552px"><span class="seal"></span></div>
  <div class="avatar" role="img" aria-label="Customer portrait" style="left:885px"><span class="seal"></span></div>
  <div class="reviewer" style="left:192px">Marco Lenn<span class="stars">★★★★★</span></div>
  <div class="reviewer" style="left:540px">Dale Corvin<span class="stars">★★★★★</span></div>
  <div class="reviewer" style="left:859px">Marco Lenn<span class="stars">★★★★★</span></div>
</section>
<div class="arrow" style="left:47px"><svg width="8" height="12" viewBox="0 0 8 12"><path d="M6 1 1 6l5 5" stroke="#333" stroke-width="1.5" fill="none"/></svg></div>
<div class="arrow" style="left:1125px"><svg width="8" height="12" viewBox="0 0 8 12"><path d="M2 1l5 5-5 5" stroke="#333" stroke-width="1.5" fill="none"/></svg></div>

<section class="contact" role="img" aria-label="Faint background of a modern glass building">
  <h2 class="section-title" style="top:55px">CONTACT <span class="accent">US</span></h2>
  <form class="form-card">
    <div class="field" style="left:26px;top:42px;width:302px">Full Name<sup>*</sup></div>
    <div class="field" style="left:344px;top:42px;width:302px">Email<sup>*</sup></div>
    <div class="field" style="left:26px;top:118px;width:302px">Phone Number<sup>*</sup></div>
    <div class="field" style="left:344px;top:118px;width:302px">Address<sup>*</sup></div>
    <div class="field" style="left:26px;top:196px;width:620px;height:84px">Message<sup>*</sup></div>
    <div class="submit">SUBMIT</div>
  </form>
</section>

<footer class="site-footer">
  <div class="footer-brand"><span class="dot"></span>Halcyon Tint</div>
  <nav class="footer-nav"><a>Auto Tinting</a><a>Commercial Tinting</a><a>Home Tinting</a><a>Paint Protection</a><a>Detailing</a><a>Contact Us</a></nav>
  <p class="copyright">Copyrights@2023.Halcyon Tinting.All Rights Reserved</p>
</footer>

</body>
</html>
```